Brightwell is a company offering Colon Hydrotherapy (or colonics)

Brightwell offers Colon Hydrotherapy using an innovative FDA approved system from the USA. The system is called the TORVA system. The clinic is based in Whangarei, Northland and is the first business of this kind for Northland.
I used to use a design from the Printlane website - a water symbol. However, I want a design that will convey freshness. I want something new and clean which conveys vitality and revitalisation .... perhaps water or bubbles but which brings across the idea of detoxing (which is what colon hydrotherapy does)
The clinic will only be completed in April so for now I have put my mobile number but once in the clinic this will need to be changed to a landline number ... the email address will also change. Thanks for any ideas you give me,
Updates

Hi. I need the name Brightwell first and foremost as this is the name of the Company Underneath this it has to say Colon Hydrotherapy to let people know what Brightwell is My name underneath that would be Miriam Holloway And all contact details to follow this. Thanks !

Target Market(s)

People who are wanting to "detox" and focusing on their health and wellbeing

Industry/Entity Type

Clinic

Contact Information for Business Card

Brightwell
Colon Hydrotherapy
Miriam Holloway
Unit B, 42c Harbour Lane, Whangarei

021 0487 3926
brightwellcare@mailnest.example

Font styles to use
Serif

Colors
cee9f6
33a6d7
86cae6

Requirements
Must have
• Stand out with colour or logo

```html
<!DOCTYPE html>
<html lang="en">
<head>
<meta charset="utf-8">
<title>Brightwell – Business Card</title>
<link rel="stylesheet" href="https://fonts.googleapis.com/css2?family=Lora:wght@400;700&display=swap">
<style>
  :root {
    --stage: #1b1b1d;
    --teal: #03a0c8;
    --blue-light: #4ab6cf;
    --blue-deep: #1a5f93;
    --ink: #1d1d1f;
    --muted: #6b6b70;
    --paper: #ffffff;
    --mark-grey: #e4e6e8;
  }
  html, body {
    margin: 0;
    width: 1200px;
    height: 1000px;
    overflow: hidden;
    background: var(--stage);
    font-family: "Lora", serif;
  }
  .canvas {
    position: relative;
    width: 1200px;
    height: 1000px;
  }
  .card {
    position: absolute;
    width: 620px;
    height: 360px;
    overflow: hidden;
    box-shadow: 0 18px 40px rgba(0,0,0,.55);
  }

  /* Back of card */
  .card-back {
    left: 520px;
    top: 110px;
    background: linear-gradient(200deg, var(--blue-light) 0%, #2d8fba 50%, var(--blue-deep) 100%);
    display: flex;
    align-items: center;
    justify-content: center;
  }
  .brand-lockup {
    display: flex;
    align-items: center;
    gap: 22px;
    color: var(--mark-grey);
  }
  .brand-dot {
    width: 74px;
    height: 74px;
    border-radius: 50%;
    background: var(--mark-grey);
  }
  .brand-name {
    font-weight: 700;
    font-size: 62px;
    letter-spacing: 4px;
    line-height: 1;
  }
  .brand-name small {
    display: block;
    font-size: 22px;
    letter-spacing: 14px;
    margin-top: 6px;
  }

  /* Front of card */
  .card-front {
    left: 60px;
    top: 500px;
    background: var(--paper);
  }
  .front-circle {
    position: absolute;
    left: -150px;
    top: -190px;
    width: 480px;
    height: 480px;
    border-radius: 50%;
    background: var(--teal);
  }
  .edge-tab {
    position: absolute;
    right: 0;
    top: 150px;
    width: 16px;
    height: 42px;
    background: var(--teal);
  }
  .contact {
    position: absolute;
    left: 338px;
    top: 112px;
    width: 266px;
    color: var(--ink);
  }
  .company {
    margin: 0;
    font-weight: 700;
    font-size: 28px;
    letter-spacing: 1px;
    color: var(--teal);
    text-transform: uppercase;
    line-height: 1;
  }
  .service {
    margin: 4px 0 8px;
    font-size: 16px;
    color: var(--muted);
  }
  .person {
    margin: 0 0 12px;
    font-size: 16px;
    font-weight: 700;
    color: var(--ink);
  }
  .address, .line {
    margin: 0;
    font-size: 14px;
    line-height: 1.4;
  }
  .address { margin-bottom: 10px; }
  .line + .line { margin-top: 6px; }
</style>
</head>
<body>
<main class="canvas">
  <section class="card card-back" aria-label="Card back">
    <div class="brand-lockup">
      <span class="brand-dot" aria-hidden="true"></span>
      <div class="brand-name">TORVA<small>SYSTEM</small></div>
    </div>
  </section>

  <section class="card card-front" aria-label="Card front">
    <div class="front-circle" aria-hidden="true"></div>
    <div class="edge-tab" aria-hidden="true"></div>
    <div class="contact">
      <h1 class="company">Brightwell</h1>
      <p class="service">Colon Hydrotherapy</p>
      <p class="person">Miriam Holloway</p>
      <p class="address">Unit B<br>42c Harbour Lane, Whangarei</p>
      <p class="line">p : 021 0487 3926</p>
      <p class="line">e : brightwellcare@mailnest.example</p>
    </div>
  </section>
</main>
</body>
</html>
```